Cover art for debut single - band name harbour of glass

Create a music release cover. The cover will be a single release (side A and B) but will only be released on digital streaming and download platforms. We have an existing image that needs to be part of the design, what is required to augment this existing image, is a logo and text for the title of the song being released. The song title is "Drift"

Target Market(s)

Any age group of music listener but likely someone who was in their teens or twenties in the 90s.

Industry/Entity Type

Music Download

Logo Text

Harbour of Glass or HoG

Font styles to use
Sans Serif
Other font styles liked:
• I like Sans Serif as basis of the font generally but I am also keen to see what can be done with "Uptight Neon" https://typevaultly.net/typefaces/48271/itc-brisk-lumen

Colors

Designer to choose colors to be used in the design.

Requirements
Must have
• I must have the image provided featured in the cover art, the logo you will design and the text for the title of the song being released.
• My initial idea was for a completely white cover with the provided image centred. The logo place perhaps in one corner and the title of the track in another corner. The song's title is "Drift" and should be textually represented on the cover.
• The finished product for the single's cover must include jpg files that are 3000 x 3000 pixels square and the follow variations:
• 4000 x 4000
• 5000 x 5000
• 6000 x 6000
• We will also need the bands name logo separately as well. To be clear the band name is Harbour of Glass but we are equally interested in the logo using the acronym HoG.

```html
<!DOCTYPE html>
<html lang="en">
<head>
<meta charset="utf-8">
<title>Harbour of Glass – Drift</title>
<link rel="stylesheet" href="https://fonts.googleapis.com/css2?family=Josefin+Sans:wght@300&family=Parisienne&display=swap">
<style>
  :root {
    --backdrop: #1c1c1c;
    --cover: #ffffff;
    --ink: #111111;
    --art-tone: #e9e9e9;
    --art-tone-edge: #dcdcdc;
  }
  * { margin: 0; padding: 0; box-sizing: border-box; }
  html, body {
    width: 1200px;
    height: 600px;
    overflow: hidden;
    background: var(--backdrop);
  }
  .stage {
    position: relative;
    width: 1200px;
    height: 600px;
  }
  .cover {
    position: absolute;
    left: 360px;
    top: 60px;
    width: 480px;
    height: 480px;
    background: var(--cover);
    box-shadow: 0 14px 30px rgba(0, 0, 0, 0.55);
    color: var(--ink);
  }
  .band-mark {
    position: absolute;
    top: 72px;
    left: 0;
    width: 100%;
    text-align: center;
    font-family: "Josefin Sans", sans-serif;
    font-weight: 300;
    color: var(--ink);
  }
  .band-mark__initials {
    display: block;
    font-size: 34px;
    line-height: 1;
    letter-spacing: 1px;
  }
  .band-mark__name {
    display: block;
    margin-top: 4px;
    font-size: 6px;
    letter-spacing: 1.2px;
    text-transform: uppercase;
  }
  .cover-artwork {
    position: absolute;
    left: 40px;
    top: 200px;
    width: 400px;
    height: 82px;
    background: linear-gradient(180deg, var(--art-tone), var(--art-tone-edge));
    border-radius: 6px;
  }
  .track-title {
    position: absolute;
    top: 368px;
    left: 0;
    width: 100%;
    text-align: center;
    font-family: "Parisienne", cursive;
    font-size: 36px;
    line-height: 1.2;
    color: var(--ink);
  }
</style>
</head>
<body>
  <div class="stage">
    <section class="cover">
      <div class="band-mark">
        <span class="band-mark__initials">HoG</span>
        <span class="band-mark__name">Harbour of Glass</span>
      </div>
      <div class="cover-artwork" role="img" aria-label="Row of seven abstract single-line ink portraits drawn in black on white"></div>
      <h1 class="track-title">Drift</h1>
    </section>
  </div>
</body>
</html>
```